Webdesign für Physiotherapie
Zielgruppe
Physiotherapie unter ganzheitlichen oder umfangreicheren Gesichtspunkten.
ANLAGE BEACHTEN!
Aufgabenstellung
Siehe Anlage!

```html
<!DOCTYPE html>
<html lang="de">
<head>
<meta charset="utf-8">
<title>Rückenschmerzen – Praxis Brenner</title>
<link href="https://fonts.googleapis.com/css2?family=Outfit:wght@400;500;600;700;800&family=Quicksand:wght@400;500;600;700&display=swap" rel="stylesheet">
<style>
:root{
  --gold:#d4ae12;
  --gold-soft:#dcbb35;
  --red:#e4342a;
  --ink:#111111;
  --text:#3a3a3a;
  --muted:#8a8a8a;
  --bg:#fafafa;
  --white:#ffffff;
}
*{box-sizing:border-box;margin:0;padding:0}
html,body{width:1200px;height:3436px;overflow:hidden}
body{background:var(--bg);font-family:"Quicksand",sans-serif;color:var(--text);position:relative}
section,header,footer,nav,article,div{position:relative}
.abs{position:absolute}
a{color:inherit;text-decoration:none}

/* top bar */
.topbar{height:41px;background:var(--gold);color:var(--white);font-family:"Outfit",sans-serif;font-size:12px;font-weight:500}
.topbar .addr{left:106px;top:13px;display:flex;gap:6px;align-items:center}
.topbar .mail{right:106px;top:13px;display:flex;gap:6px;align-items:center}

/* nav */
.nav{display:block;height:92px;background:var(--white)}
.brand{left:98px;top:34px;display:flex;align-items:center;gap:8px;font-family:"Outfit",sans-serif;font-weight:700;font-size:16px;color:var(--gold);white-space:nowrap}
.brand .dot{width:12px;height:12px;border-radius:50%;background:var(--gold)}
.menu{left:253px;top:36px;display:flex;gap:27px;font-family:"Outfit",sans-serif;font-size:15px;font-weight:500;color:var(--ink);white-space:nowrap}
.menu span{display:flex;align-items:center;gap:6px}
.nav-phone{right:100px;top:29px;display:flex;align-items:center;gap:14px;font-family:"Outfit",sans-serif;font-size:16px;font-weight:500;color:var(--ink)}
.nav-phone .ico{width:34px;height:34px;border-radius:50%;background:var(--red);display:flex;align-items:center;justify-content:center}

/* hero */
.hero{height:326px;background:linear-gradient(100deg,#3b3937 0%,#7a6e66 35%,#8d7c70 55%,#4a4643 100%)}
.hero::after{content:"";position:absolute;inset:0;background:rgba(20,18,16,.35)}
.hero h1{position:absolute;z-index:1;left:0;right:0;top:105px;text-align:center;font-family:"Outfit",sans-serif;font-weight:800;font-size:50px;color:var(--white);letter-spacing:.5px}
.btn{display:inline-flex;align-items:center;justify-content:center;font-family:"Outfit",sans-serif;font-weight:600;font-size:13px;color:var(--white);border-radius:4px}
.btn-gold{background:var(--gold)}
.btn-red{background:var(--red)}
.hero .btn{position:absolute;z-index:1;left:533px;top:184px;width:135px;height:46px}

/* service */
.service{height:768px}
.service h2{left:98px;top:108px;font-family:"Outfit",sans-serif;font-weight:700;font-size:44px;color:var(--ink)}
.price{left:566px;top:104px;display:flex;align-items:baseline;gap:18px}
.price b{font-family:"Outfit",sans-serif;font-weight:800;font-size:46px;color:var(--gold)}
.price span{font-size:14px;color:var(--text);font-weight:500}
.h3{font-family:"Outfit",sans-serif;font-weight:700;font-size:27px;color:var(--gold)}
.service .ov{left:98px;top:205px}
.copy{font-size:14px;line-height:22.5px;font-weight:500;color:var(--text)}
.service .p1{left:100px;top:262px;width:610px}
.service .p2{left:100px;top:375px;width:610px}
.service .inc{left:98px;top:502px}
.checks{display:grid;grid-template-columns:172px 172px;row-gap:10px;font-size:14px;font-weight:500;color:var(--text)}
.checks li{list-style:none;display:flex;align-items:center;gap:10px;height:19px}
.service .checks{left:100px;top:560px}
.photo{border-radius:6px}
.service .ph1{left:815px;top:103px;width:285px;height:379px;background:linear-gradient(160deg,#9fae86,#6d7663 50%,#b9b3aa)}
.service .ph2{left:731px;top:341px;width:286px;height:337px;background:linear-gradient(170deg,#cfcfcd,#8e8b88 45%,#3d3a38)}

/* reviews */
.reviews{height:528px;background:var(--gold)}
.reviews .kicker{left:101px;top:120px;font-family:"Outfit",sans-serif;font-size:17px;color:var(--white)}
.reviews .kicker b{font-weight:700}
.reviews h2{left:98px;top:150px;font-family:"Outfit",sans-serif;font-weight:700;font-size:49px;line-height:57px;color:var(--white)}
.reviews .lead{left:98px;top:285px;width:460px;font-size:14px;line-height:22.5px;color:var(--white);font-weight:500}
.reviews .btn{left:98px;top:363px;width:136px;height:46px}
.card{position:absolute;top:129px;width:250px;height:271px;background:var(--white);border-radius:4px;padding:38px 22px 0}
.card p{font-size:14px;line-height:22.5px;color:var(--muted);font-weight:500}
.card .who{position:absolute;left:22px;top:186px;display:flex;align-items:center;gap:14px}
.avatar{width:53px;height:53px;border-radius:50%;background:linear-gradient(135deg,#c9b8a4,#6f625a)}
.who b{display:block;font-family:"Outfit",sans-serif;font-weight:700;font-size:14px;color:var(--gold)}
.who span{font-size:11px;color:var(--text);font-weight:500}

/* about */
.about{height:832px}
.about .kicker{left:98px;top:168px;font-family:"Outfit",sans-serif;font-size:17px;color:var(--gold)}
.about .kicker b{font-weight:700}
.about h2{left:98px;top:202px;font-family:"Outfit",sans-serif;font-weight:700;font-size:44px;line-height:53px;color:var(--ink)}
.about .copy{left:98px;top:337px;width:500px}
.about .checks{left:100px;top:449px}
.sign{left:98px;top:570px;width:270px;height:60px;border-radius:4px;background:linear-gradient(90deg,rgba(228,52,42,.10),rgba(228,52,42,.04))}
.sign-rule{left:392px;top:577px;width:1px;height:66px;background:#d5d5d5}
.signer{left:444px;top:587px}
.signer b{display:block;font-family:"Outfit",sans-serif;font-weight:700;font-size:17px;color:var(--gold)}
.signer span{font-size:14px;font-weight:500;color:var(--text);line-height:28px}
.about .ph1{left:693px;top:275px;width:407px;height:272px;background:linear-gradient(120deg,#d8d6d2,#6d6a66 45%,#2f2d2c)}
.about .ph2{left:739px;top:498px;width:278px;height:182px;background:linear-gradient(130deg,#8c8782,#3d3b39 60%,#6c6862)}
.arrow{top:425px}

/* map */
.map{height:376px;margin:0 6px;background:linear-gradient(135deg,#e9e4cf,#dfe6d4 40%,#ece7dc 70%,#e3e6ea)}
.map .pin{left:622px;top:143px;width:82px;height:82px;border-radius:50%;background:var(--white);box-shadow:0 4px 14px rgba(0,0,0,.18);display:flex;align-items:center;justify-content:center}
.map .pin i{width:18px;height:18px;border-radius:50%;background:var(--gold)}

/* footer */
.footer{height:473px;background:var(--gold);color:var(--white)}
.fcol{top:60px}
.fcol h4{font-family:"Outfit",sans-serif;font-weight:700;font-size:19px;margin-bottom:13px}
.fcol ul{list-style:none;font-family:"Outfit",sans-serif;font-size:14px;font-weight:500}
.fcol li{height:31px;display:flex;align-items:center;gap:6px}
.contact li{height:auto;margin-bottom:20px;align-items:flex-start;gap:16px;line-height:17px}
.fcol p{font-family:"Outfit",sans-serif;font-size:13.5px;line-height:17px;font-weight:500;width:290px}
.footer .btn{position:absolute;left:815px;top:175px;width:205px;height:56px;font-size:15px;font-weight:500;gap:12px}
.frule{left:98px;top:304px;width:1002px;height:1px;background:rgba(255,255,255,.45)}
.fbrand{left:98px;top:360px;display:flex;align-items:center;gap:10px;font-family:"Outfit",sans-serif;font-weight:700;font-size:20px;color:var(--white)}
.fbrand .dot{width:14px;height:14px;border-radius:50%;background:var(--white)}
.legal{right:100px;top:403px;display:flex;gap:12px;font-family:"Outfit",sans-serif;font-size:14px;color:rgba(255,255,255,.75)}
</style>
</head>
<body>

<header>
  <div class="topbar">
    <div class="abs addr">
      <svg width="10" height="12" viewBox="0 0 10 12"><path d="M5 0a4.5 4.5 0 0 0-4.5 4.5C.5 8 5 12 5 12s4.5-4 4.5-7.5A4.5 4.5 0 0 0 5 0zm0 6.3a1.8 1.8 0 1 1 0-3.6 1.8 1.8 0 0 1 0 3.6z" fill="#fff"/></svg>
      Lindenweg 14, 33790 Halle
    </div>
    <div class="abs mail">
      <svg width="11" height="9" viewBox="0 0 11 9"><rect width="11" height="9" rx="1.5" fill="#fff"/><path d="M1 1.5l4.5 3.3L10 1.5" stroke="#d4ae12" fill="none"/></svg>
      info@praxis-beispiel.de
    </div>
  </div>
  <nav class="nav">
    <div class="abs brand"><span class="dot"></span>Praxis Brenner</div>
    <div class="abs menu">
      <span>Leistungen <svg width="10" height="6"><path d="M1 1l4 4 4-4" stroke="#111" fill="none" stroke-width="1.4"/></svg></span>
      <span>Symtome <svg width="10" height="6"><path d="M1 1l4 4 4-4" stroke="#111" fill="none" stroke-width="1.4"/></svg></span>
      <span>Über mich</span>
      <span>Blog</span>
      <span>Kontakt</span>
    </div>
    <div class="abs nav-phone">
      <span class="ico"><svg width="16" height="16" viewBox="0 0 24 24"><path d="M6.6 10.8a15.1 15.1 0 0 0 6.6 6.6l2.2-2.2c.3-.3.7-.4 1-.2 1.1.4 2.3.6 3.6.6.6 0 1 .4 1 1V20c0 .6-.4 1-1 1A17 17 0 0 1 3 4c0-.6.4-1 1-1h3.5c.6 0 1 .4 1 1 0 1.3.2 2.5.6 3.6.1.3 0 .7-.2 1z" fill="#fff"/></svg></span>
      05421 3387210
    </div>
  </nav>
</header>

<section class="hero" role="img" aria-label="Foto: Hände massieren einen Rücken">
  <h1>RÜCKENSCHMERZEN</h1>
  <a class="btn btn-gold">Termin buchen</a>
</section>

<section class="service">
  <h2 class="abs">Rückenschmerzen</h2>
  <div class="abs price"><b>45€</b><span>/ Behandlung</span></div>
  <h3 class="abs h3 ov">Übersicht</h3>
  <p class="abs copy p1">Donec feugiat lectus mi, nec scelerisque massa viverraac. Vivam vestibulum ornare imperdiet. sagittis diam. Maecenasma ximus fringilla viverra. Quisque males uada enim sed aliquam feugiat. Curabitur id sem eu velit eleifend tincidunt met con uat mielit euarcu.</p>
  <p class="abs copy p2">Curabitur et lorem et dolor iaculis convallis. Curabitur interdum ipsum convallis porttitor vulputate. Morbi sed massa at dui congue porttitor eget.</p>
  <h3 class="abs h3 inc">Inklusive &amp; Exklusive</h3>
  <ul class="abs checks">
    <li><svg width="16" height="12"><path d="M1 6l4.5 4.5L15 1" stroke="#d4ae12" fill="none" stroke-width="1.5"/></svg>Lorem ipsum</li>
    <li><svg width="16" height="12"><path d="M1 6l4.5 4.5L15 1" stroke="#d4ae12" fill="none" stroke-width="1.5"/></svg>Lorem ipsum</li>
    <li><svg width="16" height="12"><path d="M1 6l4.5 4.5L15 1" stroke="#d4ae12" fill="none" stroke-width="1.5"/></svg>Lorem ipsum</li>
    <li><svg width="14" height="14"><path d="M1 1l12 12M13 1L1 13" stroke="#d4ae12" stroke-width="1.5"/></svg>Lorem ipsum</li>
    <li><svg width="16" height="12"><path d="M1 6l4.5 4.5L15 1" stroke="#d4ae12" fill="none" stroke-width="1.5"/></svg>Lorem ipsum</li>
    <li><svg width="14" height="14"><path d="M1 1l12 12M13 1L1 13" stroke="#d4ae12" stroke-width="1.5"/></svg>Lorem ipsum</li>
  </ul>
  <div class="abs photo ph1" role="img" aria-label="Foto: Therapeut behandelt das Bein eines Patienten"></div>
  <div class="abs photo ph2" role="img" aria-label="Foto: Rückenmassage auf der Behandlungsliege"></div>
</section>

<section class="reviews">
  <p class="abs kicker">Das sagen <b>meine Patienten</b></p>
  <h2 class="abs">Bewertungen<br>meiner Kunden</h2>
  <p class="abs lead">Lorem ipsum dolor sit amet, consectetur adipiscing elit, sed do eiusmod tempor incididunt ut labore et dolore magna aliqua</p>
  <a class="abs btn btn-red">Termin buchen</a>
  <article class="card" style="left:587px">
    <p>Lorem ipsum dolor sit amet, consectetur adipiscing elit, sed do eiusmod tempor incididunt ut labore et dolore magna aliqua</p>
    <div class="who"><div class="avatar" role="img" aria-label="Porträt der Patientin"></div><div><b>Greta Lindner</b><span>Bürokauffrau</span></div></div>
  </article>
  <article class="card" style="left:850px">
    <p>Lorem ipsum dolor sit amet, consectetur adipiscing elit, sed do eiusmod tempor incididunt ut labore et dolore magna aliqua</p>
    <div class="who"><div class="avatar" role="img" aria-label="Porträt des Patienten"></div><div><b>Jonas Wetterau</b><span>Polizist</span></div></div>
  </article>
</section>

<section class="about">
  <svg class="abs arrow" style="left:27px" width="12" height="22"><path d="M11 1L1 11l10 10" stroke="#d4ae12" fill="none" stroke-width="1.6"/></svg>
  <svg class="abs arrow" style="left:1138px" width="12" height="22"><path d="M1 1l10 10L1 21" stroke="#d4ae12" fill="none" stroke-width="1.6"/></svg>
  <p class="abs kicker">Privatpraxis von <b>Lukas Brenner</b></p>
  <h2 class="abs">Die fasziale-funktionelle<br>Betrachtungsweise</h2>
  <p class="abs copy">Lorem ipsum dolor sit amet, consectetur adipiscing elit, sed do eiusmod tempor incididunt ut labore et dolore magna aliqua. Ut enim ad minim venia m, quis nostrud exercitation ullamco laboris nisi ut aliquip ex ea commodo consequat Duis aute irure dolo</p>
  <ul class="abs checks">
    <li><svg width="16" height="12"><path d="M1 6l4.5 4.5L15 1" stroke="#d4ae12" fill="none" stroke-width="1.5"/></svg>Lorem ipsum</li>
    <li><svg width="16" height="12"><path d="M1 6l4.5 4.5L15 1" stroke="#d4ae12" fill="none" stroke-width="1.5"/></svg>Lorem ipsum</li>
    <li><svg width="16" height="12"><path d="M1 6l4.5 4.5L15 1" stroke="#d4ae12" fill="none" stroke-width="1.5"/></svg>Lorem ipsum</li>
    <li><svg width="16" height="12"><path d="M1 6l4.5 4.5L15 1" stroke="#d4ae12" fill="none" stroke-width="1.5"/></svg>Lorem ipsum</li>
    <li><svg width="16" height="12"><path d="M1 6l4.5 4.5L15 1" stroke="#d4ae12" fill="none" stroke-width="1.5"/></svg>Lorem ipsum</li>
    <li><svg width="16" height="12"><path d="M1 6l4.5 4.5L15 1" stroke="#d4ae12" fill="none" stroke-width="1.5"/></svg>Lorem ipsum</li>
  </ul>
  <div class="abs sign" role="img" aria-label="Handschriftliche Unterschrift des Therapeuten"></div>
  <div class="abs sign-rule"></div>
  <div class="abs signer"><b>Lukas Brenner</b><span>Physiotherapeut</span></div>
  <div class="abs photo ph1" role="img" aria-label="Foto: Therapeut dehnt das Bein eines Patienten"></div>
  <div class="abs photo ph2" role="img" aria-label="Foto: Kniebehandlung auf der Liege"></div>
</section>

<section class="map" role="img" aria-label="Stadtplan mit dem Standort der Praxis">
  <div class="abs pin"><i></i></div>
</section>

<footer class="footer">
  <div class="abs fcol" style="left:98px">
    <h4>Quik Links</h4>
    <ul>
      <li>Leistungen <svg width="9" height="6"><path d="M1 1l3.5 3.5L8 1" stroke="#fff" fill="none" stroke-width="1.3"/></svg></li>
      <li>Symtome <svg width="9" height="6"><path d="M1 1l3.5 3.5L8 1" stroke="#fff" fill="none" stroke-width="1.3"/></svg></li>
      <li>Über mich</li>
      <li>Blog</li>
      <li>Kontakt</li>
    </ul>
  </div>
  <div class="abs fcol" style="left:313px">
    <h4>Andere Seiten</h4>
    <ul><li>Rückenschmerzen</li><li>Migräne</li><li>Massagen</li><li>Tinnitus</li></ul>
  </div>
  <div class="abs fcol contact" style="left:534px">
    <h4>Kontaktinfos</h4>
    <ul>
      <li><svg width="17" height="17" viewBox="0 0 17 17"><path d="M1 2l15 5-6 2-2 6z" stroke="#fff" fill="none" stroke-width="1.2" stroke-linejoin="round"/></svg><span>Lindenweg 14<br>33790 Halle</span></li>
      <li><svg width="16" height="16" viewBox="0 0 24 24"><path d="M6.6 10.8a15.1 15.1 0 0 0 6.6 6.6l2.2-2.2c.3-.3.7-.4 1-.2 1.1.4 2.3.6 3.6.6.6 0 1 .4 1 1V20c0 .6-.4 1-1 1A17 17 0 0 1 3 4c0-.6.4-1 1-1h3.5c.6 0 1 .4 1 1 0 1.3.2 2.5.6 3.6.1.3 0 .7-.2 1z" stroke="#fff" fill="none" stroke-width="1.6"/></svg><span>05421 3387210</span></li>
      <li><svg width="16" height="13" viewBox="0 0 16 13"><rect x=".6" y=".6" width="14.8" height="11.8" rx="1" stroke="#fff" fill="none" stroke-width="1.2"/><path d="M1 1.5l7 5.5 7-5.5" stroke="#fff" fill="none" stroke-width="1.2"/></svg><span>kontakt@praxis-beispiel.de</span></li>
    </ul>
  </div>
  <div class="abs fcol" style="left:815px">
    <h4>Jetzt Termin vereinbaren</h4>
    <p>Eine genaue Diagnose zu erhalten, kann eine der einschneidendsten Erfahrungen sein, die man machen kann.</p>
  </div>
  <a class="btn btn-red"><svg width="18" height="18" viewBox="0 0 24 24"><path d="M6.6 10.8a15.1 15.1 0 0 0 6.6 6.6l2.2-2.2c.3-.3.7-.4 1-.2 1.1.4 2.3.6 3.6.6.6 0 1 .4 1 1V20c0 .6-.4 1-1 1A17 17 0 0 1 3 4c0-.6.4-1 1-1h3.5c.6 0 1 .4 1 1 0 1.3.2 2.5.6 3.6.1.3 0 .7-.2 1z" stroke="#fff" fill="none" stroke-width="1.6"/></svg>05421 3387210</a>
  <div class="abs frule"></div>
  <div class="abs fbrand"><span class="dot"></span>Praxis Brenner</div>
  <div class="abs legal"><span>AGB's</span><span>Datenschutz</span><span>Impressum</span></div>
</footer>

</body>
</html>
```